I need 8 Banners for my Web Site

I am building an online store with prestashop, The store will sell costa rican coffee bags, I have the site almost ready, but I need some nice banners.

Top Banners
3 Banners
940x446

2 Banner
218x158

Footer Banners
3 Banners
280x100

Please see the attached images to see how they will fit in the web page.
Also you can see some of the products and images over here https://www.faceplaza-social.net/TheAmberCrate

All I need is that the banners fit with the website design, and that they look "coffee related",(think about a coffee shop with fine coffee products, fresh coffee from a latin american country, think about a mountain full of coffee plants, think about nature, think about flavor)

Colors are brown,green, gray, white, but if you see something else can match those colors feel free to use them.

Also Below the texts you must Use:

3 Banners
940x446

#1
Welcome Coffee Lovers!
The Amber Crate Store is Open Now!

#2
Fresh Coffee from the Costa Rican Mountains!
Get your coffee Now!

#3
Free Coffee Samples!
Fill our form and participate for weekly promotions!

2 Banners
218x158

#1
Carbon Neutral Coffee
Get it Now!

#2
Coffee from the TarrazĂș Mountains
Buy Now!

3 Banners
280x100

#1
Coffee from Velmira Estate Farm
Shop Now!

#2
Lurano Coffee, the finest beans to your door!
Shop Now!

#3
Check our Espresso catalog!
Shop Now!

```html
<!DOCTYPE html>
<html lang="en">
<head>
<meta charset="utf-8">
<title>Welcome Coffee Lovers – The Amber Crate</title>
<link rel="stylesheet" href="https://fonts.googleapis.com/css2?family=Montserrat:wght@300;700;800&family=Lobster&display=swap">
<style>
  :root {
    --parchment-light: #f3e6c8;
    --parchment-mid: #e6cf9f;
    --parchment-edge: #c99a5c;
    --ink: #231f20;
    --leaf-green: #0f7a3a;
    --roast-dark: #2a1409;
    --roast-mid: #5a3117;
    --roast-warm: #8a5a33;
    --cup-white: #f4f1ec;
  }
  html, body {
    margin: 0;
    padding: 0;
    overflow: hidden;
    background: #ffffff;
  }
  .banner {
    position: relative;
    width: 1200px;
    height: 569px;
    overflow: hidden;
    background:
      radial-gradient(ellipse 60% 70% at 45% 45%, var(--parchment-light) 0%, var(--parchment-mid) 55%, var(--parchment-edge) 100%);
    font-family: "Montserrat", sans-serif;
  }
  .bean-photo {
    position: absolute;
    left: 0;
    top: 0;
    width: 260px;
    height: 569px;
    background:
      linear-gradient(90deg, var(--roast-mid) 0%, var(--roast-warm) 45%, rgba(138, 90, 51, 0.35) 80%, rgba(138, 90, 51, 0) 100%);
  }
  .headline {
    position: absolute;
    left: 292px;
    width: 400px;
    top: 0;
    text-align: center;
    color: var(--ink);
  }
  .welcome {
    position: absolute;
    top: 28px;
    left: 0;
    width: 100%;
    margin: 0;
    font-family: "Lobster", cursive;
    font-size: 40px;
    font-weight: 400;
    color: var(--leaf-green);
  }
  .title {
    margin: 0;
    position: absolute;
    top: 90px;
    left: 0;
    width: 100%;
    line-height: 1;
  }
  .title-strong {
    display: block;
    font-size: 84px;
    font-weight: 800;
    letter-spacing: 1px;
  }
  .title-light {
    display: block;
    margin-top: 8px;
    font-size: 80px;
    font-weight: 300;
    letter-spacing: 1px;
  }
  .brand {
    position: absolute;
    top: 318px;
    left: 0;
    width: 100%;
    display: flex;
    justify-content: center;
    align-items: center;
    gap: 12px;
    font-size: 32px;
    font-weight: 700;
    color: var(--leaf-green);
  }
  .brand-dot {
    width: 18px;
    height: 18px;
    border-radius: 50%;
    background: var(--leaf-green);
  }
  .tagline {
    position: absolute;
    top: 442px;
    left: 0;
    width: 100%;
    margin: 0;
    font-size: 21px;
    font-weight: 700;
    color: var(--leaf-green);
  }
  .cta {
    position: absolute;
    top: 485px;
    left: 0;
    width: 100%;
    margin: 0;
    font-size: 46px;
    font-weight: 800;
    color: var(--ink);
    letter-spacing: 1px;
  }
  .cup-panel {
    position: absolute;
    left: 795px;
    top: 0;
    width: 319px;
    height: 569px;
    background:
      radial-gradient(ellipse 55% 22% at 58% 72%, var(--cup-white) 0%, rgba(244, 241, 236, 0.85) 55%, rgba(244, 241, 236, 0) 100%),
      linear-gradient(180deg, var(--roast-dark) 0%, var(--roast-mid) 55%, var(--roast-warm) 100%);
  }
</style>
</head>
<body>
  <div class="banner">
    <div class="bean-photo" role="img" aria-label="Photo of roasted coffee beans scattered along the left edge"></div>

    <div class="headline">
      <p class="welcome">Welcome</p>
      <h1 class="title">
        <span class="title-strong">COFFEE</span>
        <span class="title-light">LOVERS!</span>
      </h1>
      <div class="brand"><span class="brand-dot"></span>The Amber Crate</div>
      <p class="tagline">Costa Rican Coffee Online</p>
      <p class="cta">OPEN NOW!</p>
    </div>

    <div class="cup-panel" role="img" aria-label="Steaming white cup of black coffee on a saucer over a dark brown ornamental backdrop"></div>
  </div>
</body>
</html>
```